Fenwick Salve by Tidy Owls: All Natural Lip Balm Co. Looking for New Label

Greetings, our company is called Tidy Owls and we are a start-up founded in early 2014. We make 100% All-Natural lip balm, called Fenwick Salve, in a variety of flavors and we are looking for a new label that incorporates part of our logo and highlights our product name and our lip balms flavor (see attached files). Our website is: fenwicksalve.example, and we are on Twitter: @TidyOwlsSalves, and Facebook: /TidyOwlsSalves. Our lip balms are made with beeswax, sweet almond oil, shea butter, coconut oil and other all natural oils and flavors.

The design should be clean, and communicate comfort, its "all-natural-ness", reliability, and fun. The colors we would like to have incorporated are burgundy, a deep, but not dark orange (see files, website, logo, graphics), some green and maybe gold/yellow. Given that the lip balm tubes are small (standard tubes), we would like to assure that the lip balm name, the flavor, and part of the logo- (perhaps the bee), are clearly visible and easily read. I am open to a variety of fonts, as long as they convey what I have stated above.

We want to use the label graphics and our logo for not only labeling our product, but also for use on our website, on banners, signs, retail boxes, letterhead, tee shirts, etc. If we like the design we are open to working with you again as our company is growing and we will be expanding our product line within the year to include hand and body balms, as well as other similar items and we will eventually have a few different product lines marketed at various age groups as well. Our lip balm is currently marketed to 14 to 40+ demographic, with the average age being roughly in the 15 to 24 range and our lip balm has been purchased by more women than men, though we market to both.

As far as software goes, I would like it to be in a format that is most popular- my old logo and graphics were made in Adobe Creative Suite 5.0, Adobe InDesign, and Adobe Illustrator, so the label should be made using this software (or a higher version). If I can have the label in a JPEG format also so I personally can add it to my website and social media that would be great.

I have a label redesign doc in an indd format but it was too large to upload. I believe this was the entire layout of our last label. If you need this, or anything else, please let me know as well as how I can send it to you.

We have applied to the popular TV show Crane Court and recently received a call back with interest from the producers; we are so excited and hope you are as well!

Thank you!
Rolf Dagestad
Owner
Tidy Owls Salves LLC
Rolf@TidyOwlsSalves.example

The Label dimensions are: 2.25 inches wide ---> by 2 inches long. Currently, there is a .75 inch area that is part of the label and is perforated, used as a safety seal. I may be changing the labels to a slightly different kind but the dimensions will be the same. The tubes we use are standard lip balm tubes with a net weight of .15 ounces ( the total length of the tube from the bottom turning piece to the top of the cap is just over 2.5 inches (this is NOT how large the label must be).We are discontinuing the 1 Hive, 2 Hive concepts ( for different consistencies of the balm) so that part of the label does not need to be included.Feel free to enhance and/or modify the logo to fit the design of the label.Thank you! Added Thursday, February 12, 2015

Requirements
Must have
• Label Dimensions:
• Length: 2.125" Height: 2.125"
• Top Margin: 1.025" Bottom Margin: 1.025"
• Left Margin: 0.9125" Right Margin: 0.9125"
• Horizontal Spacing: 0.15" Vertical Spacing: 0.15"
• Horizontal Pitch: 2.275" Vertical Pitch: 2.275"

```html
<!DOCTYPE html>
<html lang="en">
<head>
<meta charset="utf-8">
<title>Fenwick Salve – Rolf's Cherry Pie Label</title>
<link href="https://fonts.googleapis.com/css2?family=Montserrat:wght@400;500;700&display=swap" rel="stylesheet">
<style>
  :root {
    --canvas: #ffffff;
    --ink: #111111;
    --gold: #f5b133;
    --burgundy: #9e0a45;
    --rose: #e899aa;
    --pattern-pink: #e3a0ae;
    --pattern-deep: #cf6479;
    --white: #ffffff;
  }
  html, body {
    margin: 0;
    padding: 0;
    width: 1200px;
    height: 1000px;
    overflow: hidden;
    background: var(--canvas);
    font-family: "Montserrat", sans-serif;
  }
  .canvas {
    position: relative;
    width: 1200px;
    height: 1000px;
  }
  .label {
    position: absolute;
    left: 191px;
    top: 154px;
    width: 818px;
    height: 691px;
    box-sizing: border-box;
    border: 1px solid var(--ink);
    background: var(--white);
    overflow: hidden;
  }
  .brand {
    position: absolute;
    left: 0;
    top: 0;
    width: 100%;
    height: 262px;
  }
  .brand-name {
    position: absolute;
    left: 0;
    right: 0;
    top: 112px;
    display: flex;
    justify-content: center;
    align-items: center;
    gap: 14px;
    font-weight: 500;
    font-size: 50px;
    line-height: 1;
    color: var(--ink);
    letter-spacing: 0.01em;
  }
  .brand-dot {
    width: 22px;
    height: 22px;
    border-radius: 50%;
    background: var(--gold);
  }
  .tagline {
    position: absolute;
    left: 0;
    right: 0;
    top: 190px;
    text-align: center;
    font-weight: 500;
    font-size: 17px;
    letter-spacing: 0.16em;
    color: var(--gold);
  }
  .flavor-band {
    position: absolute;
    left: 0;
    top: 262px;
    width: 100%;
    height: 129px;
    background: var(--burgundy);
    text-align: center;
  }
  .flavor-name {
    margin: 0;
    padding-top: 21px;
    font-weight: 700;
    font-size: 41px;
    line-height: 1;
    letter-spacing: 0.19em;
    color: var(--rose);
  }
  .product-type {
    margin: 18px 0 0;
    font-weight: 500;
    font-size: 20px;
    line-height: 1;
    letter-spacing: 0.15em;
    color: var(--white);
  }
  .pattern-field {
    position: absolute;
    left: 0;
    top: 391px;
    width: 100%;
    height: 300px;
    background: linear-gradient(180deg, var(--pattern-pink), var(--pattern-deep) 50%, var(--pattern-pink));
  }
</style>
</head>
<body>
  <main class="canvas">
    <section class="label">
      <header class="brand">
        <div class="brand-name"><span>Fenwick Salve</span><span class="brand-dot"></span></div>
        <div class="tagline">SIMPLE SWEET COMFORT</div>
      </header>
      <div class="flavor-band">
        <h1 class="flavor-name">ROLF’S CHERRY PIE</h1>
        <p class="product-type">NATURAL BEES WAX LIP BALM</p>
      </div>
      <div class="pattern-field" role="img" aria-label="Repeating pink geometric pattern of rounded bars and diamonds"></div>
    </section>
  </main>
</body>
</html>
```